BrimDesk Virtual Assistant Flyer

I need a two sided, half page flyer, for my business BrimDesk. A company description is attached in the brief. The first side needs to be mostly eye catching and witty and the other side needs to be mostly informative. I want to make sure that the eye catching side also needs to let people know that BrimDesk is a virtual assistant. If this flyer were sitting on a table with 50 other fliers, I want this one to really pop and stand out. I want it to be professional but fun. Use the exact colors from logo please.
Updates

Target Market(s)

business professionals and entrepreneurs

Industry/Entity Type

Business

Requirements
Must have
• logo
Should not have
• All of the services listed. It makes the flyer too busy

```html
<!DOCTYPE html>
<html lang="en">
<head>
<meta charset="utf-8">
<title>BrimDesk Virtual Assistant Flyer</title>
<link href="https://fonts.googleapis.com/css2?family=Open+Sans:ital,wght@0,400;0,600;0,700;0,800;1,400;1,600;1,700;1,800&display=swap" rel="stylesheet">
<style>
  :root {
    --backdrop: #dcdcdc;
    --paper: #efeff0;
    --ink: #1a1a1a;
    --green: #76bc3a;
    --red: #c33b2b;
    --teal: #3a9ea5;
    --photo-light: #c9d6b8;
    --photo-dark: #7c8f62;
    --fold: #e2e2e4;
  }
  * { margin: 0; padding: 0; box-sizing: border-box; }
  html, body { width: 1200px; height: 800px; overflow: hidden; }
  body {
    background: var(--backdrop);
    font-family: "Open Sans", Arial, sans-serif;
    color: var(--ink);
    position: relative;
  }
  .page {
    position: absolute;
    top: 60px;
    width: 404px;
    height: 585px;
    background: var(--paper);
    transform: scale(1.163);
    transform-origin: top left;
    overflow: hidden;
  }
  .page--front { left: 110px; }
  .page--back { left: 620px; }

  /* Front */
  .front-art { position: absolute; inset: 0; }
  .brand {
    position: absolute; top: 24px; right: 16px;
    display: flex; align-items: center; gap: 4px;
    font-weight: 800; font-size: 15px; color: var(--ink); letter-spacing: -0.3px;
  }
  .brand__dot { width: 8px; height: 8px; background: var(--red); }
  .headline {
    position: absolute; left: 22px; top: 52px;
    font-size: 14.5px; font-weight: 800; font-style: italic; line-height: 20px;
  }
  .intro {
    position: absolute; left: 21px; top: 94px; width: 186px;
    font-size: 7.2px; font-style: italic; line-height: 11.2px;
  }
  .intro p + p { margin-top: 11px; }
  .summary-title {
    position: absolute; left: 17px; top: 268px;
    font-size: 18px; font-weight: 800; line-height: 18px;
  }
  .summary-text {
    position: absolute; left: 18px; top: 314px; width: 205px;
    font-size: 4.6px; line-height: 7.3px; text-align: justify;
  }
  .statement { position: absolute; left: 21px; width: 180px; }
  .statement h3 { font-size: 6.4px; font-weight: 800; margin-bottom: 2px; }
  .statement p { font-size: 5px; font-style: italic; line-height: 8.2px; }
  .statement--mission { top: 415px; }
  .statement--values { top: 452px; }
  .statement--slogan { top: 496px; }
  .contact { position: absolute; left: 262px; top: 476px; }
  .contact h3 { font-size: 12.5px; font-weight: 800; margin-bottom: 5px; letter-spacing: 0.2px; }
  .contact p { font-size: 5.8px; font-weight: 700; line-height: 7.8px; }
  .color-band { position: absolute; left: 0; bottom: 0; width: 100%; height: 15px; display: flex; }
  .color-band span { flex: 1; }
  .color-band .green { background: var(--green); }
  .color-band .red { background: var(--red); }
  .color-band .teal { background: var(--teal); }

  /* Back */
  .bulb-strip {
    position: absolute; left: 0; top: 0; width: 50px; height: 100%;
    background: linear-gradient(180deg, #d9d9d9 0%, #c84a3c 12%, #d4d4d4 22%, #7cc04a 30%, #d6d6d6 40%, #c84a3c 50%, #d2d2d2 60%, #7cc04a 70%, #d4d4d4 80%, #c84a3c 90%, #d9d9d9 100%);
    opacity: 0.85;
  }
  .back-content { position: absolute; left: 63px; right: 20px; top: 0; bottom: 0; }
  .block-center { text-align: center; }
  .block-title { font-size: 8px; font-weight: 700; }
  .intro-list {
    list-style: none; font-size: 4.8px; font-style: italic; line-height: 6.4px; margin-top: 2px;
  }
  .know-you { position: absolute; top: 23px; left: 0; right: 0; }
  .benefits { position: absolute; top: 97px; left: 0; right: 0; }
  .benefits p { font-size: 4.8px; font-style: italic; line-height: 6.4px; margin-top: 3px; padding: 0 8px; }
  .services-title { position: absolute; top: 161px; left: 3px; font-size: 8.6px; font-weight: 700; }
  .service { position: absolute; left: 0; width: 290px; font-size: 8.6px; line-height: 10.2px; }
  .service strong { font-weight: 700; }
  .service--content { top: 195px; }
  .service--organize { top: 268px; width: 250px; }
  .service--events { top: 327px; }
  .service--travel { top: 371px; width: 265px; }
  .service--mailings { top: 415px; }
  .back-cta {
    position: absolute; top: 492px; left: 24px; right: 24px;
    font-size: 5px; font-weight: 700; font-style: italic; line-height: 6.6px;
  }
  .back-address {
    position: absolute; top: 547px; left: 0; right: 0;
    font-size: 3.8px; font-weight: 700; line-height: 5.2px;
  }
</style>
</head>
<body>
  <section class="page page--front" aria-label="Flyer front">
    <svg class="front-art" viewBox="0 0 404 585" width="404" height="585">
      <defs>
        <linearGradient id="photoTone" x1="0" y1="0" x2="1" y2="1">
          <stop offset="0" stop-color="var(--photo-dark)"/>
          <stop offset="0.55" stop-color="var(--photo-light)"/>
          <stop offset="1" stop-color="#e8d6cc"/>
        </linearGradient>
      </defs>
      <polygon points="170,262 285,328 225,318" fill="var(--fold)"/>
      <polygon points="380,88 170,216 170,262 285,328 380,272" fill="url(#photoTone)" role="img" aria-label="Photo of a smiling woman on the phone at a laptop"/>
      <polygon points="133,238 170,216 170,262" fill="var(--green)"/>
      <polygon points="285,328 380,272 380,380" fill="var(--red)"/>
      <polygon points="285,328 380,380 285,435" fill="var(--teal)"/>
    </svg>

    <div class="brand"><span class="brand__dot"></span>BrimDesk</div>

    <h1 class="headline">THE TIME TO<br>ACT IS NOW!</h1>
    <div class="intro">
      <p>We are committed to becoming your irreplaceable virtual resource. So stop falling farther behind &amp; expand your business virtually.</p>
      <p>We want to assist you in getting your business where you want it to be.</p>
    </div>

    <h2 class="summary-title">BUSINESS<br>SUMMARY</h2>
    <p class="summary-text">BrimDesk provides business professionals with critical administrative and management support, virtually. We know it can be time consuming and confusing to stay organized and up to date in today's fast paced digital world. With that in mind, it is more crucial than ever to keep current in all of the rapidly changing parts of modern business. That's where BrimDesk comes in, with fresh, practical ways to help. We take the time to learn the ins and outs of your business needs and are here to assist in many ways. Whatever you can't or don't have time to do is exactly what we are here for. This frees up time for you to do the things only you can do.</p>

    <div class="statement statement--mission">
      <h3>MISSION STATEMENT</h3>
      <p>BrimDesk provides administrative &amp; management<br>support for business professionals, virtually.</p>
    </div>
    <div class="statement statement--values">
      <h3>VALUES STATEMENT</h3>
      <p>We are committed to become your invaluable virtual resource by providing revolutionary, quality services to expand your business virtually and save your valuable time.</p>
    </div>
    <div class="statement statement--slogan">
      <h3>SLOGAN</h3>
      <p>Expanding Business Virtually.<br>Some call them super human, we call them virtual assistants!<br>Whatever you can't, won't or don't have time to do, is exactly what we are here for!</p>
    </div>

    <div class="contact">
      <h3>CONTACT US</h3>
      <p>P.O. Box 480217 Austin, Texas 78701<br>(512) 555-0187<br>hello@brimdesk.biz<br>brimdesk.biz</p>
    </div>

    <div class="color-band"><span class="green"></span><span class="red"></span><span class="teal"></span></div>
  </section>

  <section class="page page--back" aria-label="Flyer back">
    <div class="bulb-strip" role="img" aria-label="Pattern of red, green, teal and grey light bulbs"></div>
    <div class="back-content">
      <div class="know-you block-center">
        <h2 class="block-title">Getting to Know You &amp; Your Business</h2>
        <ol class="intro-list">
          <li>1. Describe your occupation: Company, Industry, job duties, etc.</li>
          <li>2. What are your biggest 'time sucking' or most disliked tasks?</li>
          <li>3. What is the #1 goal that you want to achieve in 2017?</li>
          <li>4. Do you currently outsource tasks, via employees or virtually?</li>
        </ol>
      </div>
      <div class="benefits block-center">
        <h2 class="block-title">Benefits to Expect From BRIMDESK a Virtual Assistant:</h2>
        <p>No turnover or wasted time training new in-office assistants. No in-office devices, supplies, physical space or benefits cost. No employee management or training resources needed. Fewer hours spent learning the new aspects of the digital world.</p>
      </div>

      <h2 class="services-title">SERVICE OPTIONS FOR WHAT YOU NEED MOST</h2>
      <p class="service service--content"><strong>Virtual Content –</strong> Optimize the efficiency and look of your text documents, data spreadsheets, emails, reports, slide presentations, cover letters, meeting prep/notes, resumes, contracts, etc.</p>
      <p class="service service--organize"><strong>Virtual Organization –</strong> Make the jump to digital organization<br>and wonder how you lived without it.</p>
      <p class="service service--events"><strong>Event Planning –</strong> Coordination with vendors to organize small business events.</p>
      <p class="service service--travel"><strong>Travel Arrangements –</strong> Coordinating all aspects of business travel</p>
      <p class="service service--mailings"><strong>Client Mailings –</strong> A one-time mailing, mass mailing to all of your clients or anywhere in between.</p>

      <p class="back-cta block-center">Please email hello@brimdesk.biz to give us the opportunity to show you the ways a virtual assistant at BrimDesk will be the perfect fit to expand your business virtually!</p>
      <p class="back-address block-center">P.O. Box 480217 Austin, Texas 78701 | (512) 555-0187<br>hello@brimdesk.biz · brimdesk.biz</p>
    </div>
  </section>
</body>
</html>
```